Flyer Design Project

I need an a5 sized flyer designed for my companys Mindfulness Based Stress Reduction course. I would like it to look peaceful but I would like the designer to be a little creative I don't want it to look like every other boring wellness brochure. No cliched images please. The course is about Mindfulness, there is yoga and meditation involved, again don't want your typical yoga and meditation images on it. I want it to look interesting and different.

The attached document has two pages each page should be one side of the leaflet.

Target Market(s)

alternative people who are interested in wellness, stressed out people and people who have health issues and could benefit from Mindfulness

Industry/Entity Type

Wellness

Requirements
Must have
• I want the fact that we are donating to charity to be obvious. But not in a showing off way. I want it known but NOT hey look at how wonderful I am.

Nice to have
• The font similar to my website.

http://www.quietbirchgrovewellness.com
Should not have
• Cheesy cliched images of yoga and meditation.

```html
<!DOCTYPE html>
<html lang="en">
<head>
<meta charset="utf-8">
<title>Mindfulness Based Stress Reduction – Flyer</title>
<link href="https://fonts.googleapis.com/css2?family=PT+Sans:wght@400;700&display=swap" rel="stylesheet">
<style>
  :root{
    --bg:#f1f1ee;
    --cream:#fdf6c0;
    --cream-light:#fffbe0;
    --green:#1f9a46;
    --green-text:#2aa247;
    --ink:#1d1d1b;
    --orange:#f2a15a;
    --yellow:#f7e53c;
    --lime:#b6d56e;
    --sky:#5fc6dd;
    --violet:#c27bbd;
    --coral:#ee8452;
    --photo-blue:#4f93cf;
    --photo-deep:#2a5f98;
  }
  *{box-sizing:border-box;margin:0;padding:0}
  html,body{width:1200px;height:845px;overflow:hidden;background:var(--bg)}
  body{font-family:"PT Sans",sans-serif;color:var(--ink);position:relative}

  .flyer-page{
    position:absolute;top:26px;width:560px;height:792px;
    background:linear-gradient(180deg,var(--cream-light) 0%,var(--cream) 70%);
    overflow:hidden;box-shadow:0 4px 14px rgba(0,0,0,.18);
  }
  .page-front{left:30px}
  .page-back{left:610px}

  .header-art{
    position:absolute;left:0;top:0;width:100%;height:100px;
    background:linear-gradient(90deg,var(--orange) 0%,var(--yellow) 22%,var(--lime) 40%,var(--sky) 56%,var(--violet) 72%,var(--coral) 88%,var(--yellow) 100%);
    opacity:.85;
  }
  .title-band{
    position:absolute;left:0;top:100px;width:100%;height:64px;
    background:var(--green);color:#fff;
    font-size:25px;line-height:64px;padding-left:28px;letter-spacing:.2px;
  }
  .feature-photo{
    position:absolute;right:26px;top:18px;width:120px;height:120px;border-radius:50%;
    border:4px solid #fff;
    background:linear-gradient(180deg,var(--photo-blue) 0%,var(--photo-deep) 100%);
    box-shadow:0 2px 6px rgba(0,0,0,.25);
  }

  .page-body{position:absolute;left:30px;right:30px;top:184px;font-size:14.2px;line-height:1.32}
  .section-heading{color:var(--green-text);font-size:15.5px;font-weight:400;margin:0 0 6px}
  .page-body p{margin:0 0 10px}
  .bullet-list{list-style:none;margin:0 0 12px 14px}
  .bullet-list li{position:relative;padding-left:14px}
  .bullet-list li::before{content:"";position:absolute;left:0;top:8px;width:5px;height:5px;border-radius:50%;background:var(--ink)}
  strong{font-weight:700}

  .footer-art{
    position:absolute;left:0;bottom:0;width:100%;height:100px;
    background:linear-gradient(90deg,var(--orange) 0%,var(--yellow) 25%,var(--lime) 45%,var(--sky) 60%,var(--violet) 75%,var(--coral) 90%,var(--yellow) 100%);
    -webkit-mask-image:linear-gradient(180deg,transparent 0%,rgba(0,0,0,.5) 100%);
    mask-image:linear-gradient(180deg,transparent 0%,rgba(0,0,0,.5) 100%);
  }

  .charity-note{
    margin:22px auto 0;width:330px;border:2px solid var(--green);
    text-align:center;padding:8px 10px;font-size:15px;line-height:1.3;background:var(--cream-light);
  }
  .web-cta{text-align:center;margin-top:40px;font-size:15px}
  .web-cta a{color:var(--green-text);text-decoration:none;display:block}
  .brand-tag{
    position:absolute;right:28px;bottom:56px;width:104px;padding:12px 8px;background:#fff;
    text-align:center;color:var(--green);font-size:14px;line-height:1.2;z-index:1;
  }
  .brand-tag .brand-square{display:block;width:26px;height:26px;background:var(--green);margin:0 auto 8px}
</style>
</head>
<body>

<section class="flyer-page page-front">
  <div class="header-art" role="img" aria-label="Decorative sunburst of coloured rays"></div>
  <div class="title-band">Mindfulness Based Stress Reduction</div>
  <div class="feature-photo" role="img" aria-label="Photo of stones balanced on a rock by the sea"></div>

  <div class="page-body">
    <h2 class="section-heading">What is Mindfulness?</h2>
    <p>Put simply, mindfulness is about being aware of the present moment, without being caught up in ruminating thoughts or worrying about the past or the future. Mindlessness can result in loss of awareness and in you becoming disconnected from your life. Mindfulness gives us the ability to live more fully as it allows the body and mind to become calmer and more aware.</p>

    <h2 class="section-heading">What is Mindfulness Based Stress Reduction (MBSR)?</h2>
    <p>MBSR uses mindful mediation and mindful movement as its basis. The practises have shown over two decades to be transforming in the lives of countless course attendees.</p>
    <p>Published reports point out that the majority of course attendees who complete the 8 weeks:</p>
    <ul class="bullet-list">
      <li>Are more aware</li>
      <li>Have decreased physical and psychological symptoms</li>
      <li>Are able to relax and manage stress</li>
      <li>Have reduced pain levels or an improved ability to cope with pain levels that may or may not go away</li>
      <li>Live more fully</li>
      <li>Have improved self esteem and reduced anxiety</li>
      <li>Are able to cope better in stressful situations</li>
    </ul>
    <p>Our MBSR courses are closely structured on the approach developed by <strong>Dr Alan Morrow</strong> and his associates at the <strong>Halden University Medical Centre.</strong></p>
  </div>
  <div class="footer-art" role="img" aria-label="Soft coloured floor of light"></div>
</section>

<section class="flyer-page page-back">
  <div class="header-art" role="img" aria-label="Decorative sunburst of coloured rays"></div>
  <div class="title-band">Mindfulness Based Stress Reduction Course</div>

  <div class="page-body">
    <p>The Mindfulness Based Stress Reduction course offered by Quiet Birch Grove Wellness provides students with a basis in understanding mindfulness, through mediation and body movement. It allows students a learning environment that is safe and inclusive of all types of people.</p>

    <h2 class="section-heading">During the 8 week course, students will have access to the following:</h2>
    <ul class="bullet-list">
      <li>2 hour weekly sessions and a daylong retreat at week 7.</li>
      <li>Guided instruction in formal and informal mindfulness practise.</li>
      <li>Mindfulness movement exercises.</li>
      <li>Activities in applying mindfulness to everyday living.</li>
      <li>Personal guidance and peer support via a secure online forum.</li>
      <li>Daily assignments.</li>
      <li>A FREE copy of Living Fully Present by Alan Morrow</li>
      <li>FREE mp3 and instructional movement videos to download</li>
    </ul>

    <div class="charity-note">10% of this course is donated to charity<br>– For this month’s charitable cause</div>

    <div class="web-cta">please see our website for details –
      <a href="http://www.quietbirchgrovewellness.com">www.quietbirchgrovewellness.com</a>
    </div>
  </div>

  <div class="brand-tag"><span class="brand-square"></span>Quiet Birch Grove Wellness</div>
  <div class="footer-art" role="img" aria-label="Soft coloured floor of light"></div>
</section>

</body>
</html>
```